Business Card for Ferncliff Massage

I need a business card for my massage therapy & cannabis oil practice. I already have a logo,the "massage" got edited out of this file. I will send the original soon. I need these elements to be on the card:
web: FerncliffMassage.example
ph: 417/283-9061
email: Mirela.Dawkant@mailbox.example
Other slogans, statements to consider:
Science Geek, Massage Therapist, Neuromuscular Therapy, Cannabis Spa Treatments, Raindrop Therapy, Essential Oils
Target Market(s)
women between 20 & 65, people with enough $ to afford regular massage, people who recently had a motor vehicle accident, Halvora HMP insured
Industry/Entity Type
Massage Therapy
Contact Information for Business Card
I would like to see my bear logo featured; contact details, greens & blues preferred colors.

```html
<!DOCTYPE html>
<html lang="en">
<head>
<meta charset="utf-8">
<title>Ferncliff Massage – Business Card</title>
<link rel="stylesheet" href="https://fonts.googleapis.com/css2?family=Cinzel:wght@500&family=Montserrat:wght@400;500&family=Ubuntu:wght@400&display=swap">
<style>
  :root {
    --stage: #1d1f1e;
    --card-green: #2f8a42;
    --accent-blue: #1a74bd;
    --ink-green: #2c8a3c;
    --paper: #ffffff;
    --stone: #9a8578;
    --white: #ffffff;
  }
  * { box-sizing: border-box; margin: 0; padding: 0; }
  html, body { width: 1200px; height: 900px; overflow: hidden; }
  body {
    background: var(--stage);
    display: flex;
    flex-direction: column;
    align-items: center;
    justify-content: center;
    gap: 48px;
  }
  .card {
    position: relative;
    width: 660px;
    height: 378px;
    overflow: hidden;
    box-shadow: 0 12px 30px rgba(0,0,0,.5);
  }

  /* Front */
  .card-front { background: var(--card-green); color: var(--white); }
  .accent-bar {
    position: absolute;
    height: 9px;
    width: 72px;
    background: var(--accent-blue);
  }
  .accent-bar--right { right: 0; top: 62px; }
  .accent-bar--left { left: 0; bottom: 48px; }
  .brand {
    position: absolute;
    top: 92px;
    left: 0; right: 0;
    display: flex;
    align-items: center;
    justify-content: center;
    gap: 16px;
  }
  .brand-dot {
    width: 54px; height: 54px;
    border-radius: 50%;
    background: var(--stone);
  }
  .brand-name {
    font-family: "Ubuntu", sans-serif;
    font-weight: 400;
    font-size: 58px;
    letter-spacing: 1px;
    color: var(--white);
  }
  .services {
    position: absolute;
    left: 0; right: 0;
    top: 236px;
    text-align: center;
    font-family: "Montserrat", sans-serif;
    font-size: 15.5px;
    line-height: 1.6;
    letter-spacing: .3px;
  }
  .services .sep { margin: 0 5px; font-size: 10px; vertical-align: 2px; }

  /* Back */
  .card-back { background: var(--paper); }
  .frame-vertical {
    position: absolute;
    left: 30px; top: 34px;
    width: 2px; height: 218px;
    background: var(--accent-blue);
  }
  .frame-horizontal {
    position: absolute;
    left: 30px; right: 26px; top: 250px;
    height: 2px;
    background: var(--accent-blue);
  }
  .back-brand {
    position: absolute;
    left: 70px; top: 76px;
    display: flex;
    align-items: center;
    gap: 14px;
  }
  .back-brand .brand-dot { width: 90px; height: 90px; }
  .back-brand .brand-name { color: var(--stone); font-size: 44px; }
  .person-name {
    position: absolute;
    right: 32px; top: 206px;
    font-family: "Cinzel", serif;
    font-weight: 500;
    font-size: 27px;
    letter-spacing: 2px;
    color: var(--ink-green);
  }
  .contact {
    position: absolute;
    left: 34px; top: 268px;
    list-style: none;
    font-family: "Montserrat", sans-serif;
    font-weight: 500;
    font-size: 19px;
    color: var(--ink-green);
  }
  .contact li { display: flex; align-items: center; gap: 10px; line-height: 32px; }
  .contact svg { width: 14px; height: 14px; fill: var(--accent-blue); flex: none; }
  .contact .web { color: var(--accent-blue); }
</style>
</head>
<body>

  <section class="card card-front">
    <span class="accent-bar accent-bar--right"></span>
    <span class="accent-bar accent-bar--left"></span>
    <div class="brand">
      <span class="brand-dot"></span>
      <span class="brand-name">Ferncliff</span>
    </div>
    <p class="services">
      Science Geek<span class="sep">●</span>Massage Therapist<span class="sep">●</span>Neuromuscular Therapy<br>
      Cannabis Spa Treatments<span class="sep">●</span>Raindrop Therapy<span class="sep">●</span>Essential Oils
    </p>
  </section>

  <section class="card card-back">
    <span class="frame-vertical"></span>
    <span class="frame-horizontal"></span>
    <div class="back-brand">
      <span class="brand-dot"></span>
      <span class="brand-name">Ferncliff</span>
    </div>
    <h1 class="person-name">MIRELA DAWKANT</h1>
    <ul class="contact">
      <li>
        <svg viewBox="0 0 24 24" aria-hidden="true"><path d="M6.6 10.8a15.1 15.1 0 0 0 6.6 6.6l2.2-2.2c.3-.3.7-.4 1-.2 1.1.4 2.3.6 3.6.6.6 0 1 .4 1 1V20c0 .6-.4 1-1 1A17 17 0 0 1 3 4c0-.6.4-1 1-1h3.5c.6 0 1 .4 1 1 0 1.3.2 2.5.6 3.6.1.3 0 .7-.2 1z"/></svg>
        417 283-9061
      </li>
      <li>
        <svg viewBox="0 0 24 24" aria-hidden="true"><path d="M2 5h20v14H2zm2 2v.5l8 5 8-5V7zm0 2.8V17h16V9.8l-8 5z"/></svg>
        Mirela.Dawkant@mailbox.example
      </li>
      <li class="web">
        <svg viewBox="0 0 24 24" aria-hidden="true"><path d="M12 2a10 10 0 1 0 0 20 10 10 0 0 0 0-20zm6.9 6h-2.9a15 15 0 0 0-1.3-3.9A8 8 0 0 1 18.9 8zM12 4c.8 1.1 1.5 2.5 1.9 4h-3.8c.4-1.5 1.1-2.9 1.9-4zM4.3 14a8 8 0 0 1 0-4h3.4a16 16 0 0 0 0 4zm.8 2h2.9c.3 1.4.8 2.7 1.3 3.9A8 8 0 0 1 5.1 16zM8 8H5.1a8 8 0 0 1 4.2-3.9C8.8 5.3 8.3 6.6 8 8zm4 12c-.8-1.1-1.5-2.5-1.9-4h3.8c-.4 1.5-1.1 2.9-1.9 4zm2.3-6H9.7a14 14 0 0 1 0-4h4.6a14 14 0 0 1 0 4zm.4 5.9c.5-1.2 1-2.5 1.3-3.9h2.9a8 8 0 0 1-4.2 3.9zm1.6-5.9a16 16 0 0 0 0-4h3.4a8 8 0 0 1 0 4z"/></svg>
        www.ferncliffmassage.example
      </li>
    </ul>
  </section>

</body>
</html>
```